Pipe and Drape Company Web site

Name of client is "Lumen Curtain" with a tagline of, "Fine Fabric, Finer Care." which will need to go across the middle of the header area. Logo will be on the left. Connectors on the right. Connectors being, join newsletter, facebook, twitter, linked In, etc...

Please refer to www.folvarstage.example for feel and layout and then www.tolmerhawks.example for background imagery style and preferred color scheme. Colors for the site should be black and dark purple with sub page text areas being white with black text. Yet still surrounded with black framing and purple infused background. We'll need a Large impactful main image area to display scrolling images. Below that will be 4 content area boxes with each of the following titles. "Corporate Events" , "Weddings" , "Special Events" , and "Products".

Main nav will need to be across the top of main image and include the 5 following tabs: "Lumen Experience", "DrapeRental" , "Gallery" , "Resources" ,
"Contact Us". Also leave a blank space on the right end of main nav in case we decide to add a 6th main nav at a later date.

This is a nationwide company and is a leader in their industry. The site should look very high end and classy. Highest quality and largest selection of drape anywhere. It should convey dependability, professionalism, Trustworthy, and expertise.

The main calls to action should be to get the visitor to call the phone number, or contact via email.

Main visitor demographic will be female event coordinators.

Sub Page design will vary based on the market segment chosen from home page. However, we feel the "wedding" category would be a good option since those pages might have a lighter look and feminine feel to them. Be sure to make it simple for the visitor to go back from the sub page, to the hame page via nav choices, or market segment boxes across the bottom again.

```html
<!DOCTYPE html>
<html lang="en">
<head>
<meta charset="utf-8">
<title>Lumen Curtain</title>
<link href="https://fonts.googleapis.com/css2?family=Arimo:wght@400;700&display=swap" rel="stylesheet">
<style>
:root{
  --page-deep:#02031a;
  --page-blue:#0d1a7a;
  --header-black:#020203;
  --nav-purple-top:#3a0f44;
  --nav-purple-bottom:#24062b;
  --panel-purple:#3c0a45;
  --panel-black:#141414;
  --heading-purple:#3d0b4a;
  --text-dark:#1a1a1a;
  --text-body:#222;
  --logo-lilac:#d9b4e6;
  --tagline-grey:#cfcfcf;
  --nav-active:#8a2a9c;
  --white:#ffffff;
  --divider:#c9b6cf;
  --curtain-red:#b3140f;
  --curtain-deep:#7a0907;
  --curtain-warm:#b8381c;
}
*{margin:0;padding:0;box-sizing:border-box}
html,body{width:1200px;height:961px;overflow:hidden}
body{
  position:relative;
  font-family:"Arimo",Arial,sans-serif;
  background:
    radial-gradient(ellipse 260px 900px at 60px 480px,rgba(40,60,200,.55),transparent 70%),
    radial-gradient(ellipse 260px 900px at 1140px 480px,rgba(40,60,200,.55),transparent 70%),
    radial-gradient(ellipse 700px 70px at 600px 945px,rgba(150,30,170,.6),transparent 75%),
    linear-gradient(90deg,var(--page-deep),var(--page-blue) 10%,var(--page-deep) 22%,var(--page-deep) 78%,var(--page-blue) 90%,var(--page-deep));
}
.site{position:absolute;left:115px;top:0;width:970px;height:911px;background:var(--white)}
.masthead{position:absolute;left:0;top:0;width:970px;height:110px;background:var(--header-black)}
.brand-name{position:absolute;left:26px;top:16px;font-size:38px;color:var(--logo-lilac);font-weight:400;letter-spacing:-.5px}
.brand-tagline{position:absolute;left:24px;top:79px;font-size:15px;color:var(--tagline-grey)}
.connectors{position:absolute;right:20px;top:52px;display:flex;gap:11px}
.connector{width:31px;height:32px;border-radius:3px;background:linear-gradient(#6f86c4,#2f4d93)}
.connector--teal{background:linear-gradient(#7fd2f0,#2a9fd0)}
.main-nav{position:absolute;left:0;top:111px;width:970px;height:44px;background:linear-gradient(var(--nav-purple-top),var(--nav-purple-bottom));display:flex;align-items:center}
.main-nav a{color:var(--white);text-decoration:none;font-size:14px;margin-left:18px;margin-right:14px}
.main-nav a.is-active{color:var(--nav-active)}
.call-box{position:absolute;right:0;top:0;width:271px;height:44px;background:var(--header-black);color:var(--white);font-size:19px;line-height:44px;padding-right:11px;text-align:right;white-space:nowrap}
.call-box strong{font-size:23px}
.hero{position:absolute;left:11px;top:165px;width:948px;height:283px;
  background:linear-gradient(90deg,var(--curtain-warm),var(--curtain-red) 18%,var(--curtain-deep) 50%,var(--curtain-red) 82%,var(--curtain-warm));}
.segments{position:absolute;left:11px;top:459px;width:948px;display:flex;gap:6px}
.segment{width:233px;height:134px;border:1px solid var(--panel-purple);background:linear-gradient(#fff,#e9e9e9)}
.segment--dark{border-color:#555}
.segment h2{height:33px;line-height:33px;padding-left:10px;font-size:16px;font-weight:400;color:var(--white);background:linear-gradient(#5a1466,var(--panel-purple))}
.segment--dark h2{background:linear-gradient(#3a3a3a,var(--panel-black))}
.segment ul{list-style:none;padding:8px 0 0 11px}
.segment li{font-size:12px;color:var(--text-body);line-height:20px}
.segment li::before,.services li::before{content:"▪";font-size:8px;margin-right:7px;vertical-align:2px}
.welcome{position:absolute;left:8px;top:606px;width:700px}
.welcome h1{font-size:20px;color:var(--heading-purple);margin-left:2px;margin-bottom:7px}
.welcome p{font-size:12px;line-height:18px;color:var(--text-body);margin-bottom:10px;margin-left:2px}
.welcome p.lead{width:678px}
.welcome p.flush{margin-left:0}
.welcome h3{font-size:16px;color:var(--text-dark);margin:21px 0 5px 2px}
.services{list-style:none;padding-left:17px}
.services li{font-size:12px;line-height:20px;color:var(--text-body)}
.column-rule{position:absolute;left:723px;top:605px;width:1px;height:300px;background:linear-gradient(var(--white),var(--divider) 20%,var(--divider) 80%,var(--white))}
.newsletter{position:absolute;left:726px;top:624px;width:250px;text-align:center}
.newsletter h2{font-size:23px;color:#000}
.newsletter h2 span{color:var(--heading-purple)}
.newsletter-art{width:112px;height:110px;margin:12px auto 0;border-radius:8px;background:linear-gradient(135deg,#ead8f2,#b27fce)}
.newsletter-submit{display:block;margin-top:26px;font-size:17px;color:#000}
.footer-note{position:absolute;right:116px;top:925px;font-size:14px;color:var(--white)}
</style>
</head>
<body>
<div class="site">
  <header class="masthead">
    <div class="brand-name">Lumen Curtain</div>
    <div class="brand-tagline">Fine Fabric, Finer Care.</div>
    <div class="connectors">
      <span class="connector" aria-label="Social link"></span>
      <span class="connector" aria-label="Social link"></span>
      <span class="connector connector--teal" aria-label="Social link"></span>
    </div>
  </header>
  <nav class="main-nav">
    <a href="#">Lumen Experience</a>
    <a href="#">DrapeRental</a>
    <a href="#" class="is-active">Gallery</a>
    <a href="#">Resources</a>
    <a href="#">Contact Us</a>
    <a href="#">Extra link</a>
    <div class="call-box">Call us : <strong>+1 555 018 274</strong></div>
  </nav>
  <div class="hero" role="img" aria-label="Photo of red stage drapes with patterned tie-back curtains"></div>
  <section class="segments">
    <div class="segment segment--dark"><h2>Corporate Events</h2><ul><li>Lorem ipsum dolor sit amet</li><li>Duis at tortor interdum arcu</li><li>Donec sollicitudin libero eu</li><li>Mauris nec quam in mi ornare</li></ul></div>
    <div class="segment"><h2>Weddings</h2><ul><li>Lorem ipsum dolor sit amet</li><li>Duis at tortor interdum arcu</li><li>Donec sollicitudin libero eu</li><li>Mauris nec quam in mi ornare</li></ul></div>
    <div class="segment segment--dark"><h2>Special Events</h2><ul><li>Lorem ipsum dolor sit amet</li><li>Duis at tortor interdum arcu</li><li>Donec sollicitudin libero eu</li><li>Mauris nec quam in mi ornare</li></ul></div>
    <div class="segment"><h2>Products</h2><ul><li>Lorem ipsum dolor sit amet</li><li>Duis at tortor interdum arcu</li><li>Donec sollicitudin libero eu</li><li>Mauris nec quam in mi ornare</li></ul></div>
  </section>
  <main class="welcome">
    <h1>Welcome to Lumen Curtain</h1>
    <p class="lead">Lorem ipsum dolor sit amet, consectetur adipiscing elit. Pellentesque lacinia metus at nisi consectetur tristique. Etiam vitae elit non mauris hendrerit sodales id pellentesque quam. Vestibulum ornare odio quis lorem viverra vitae tristique nibh faucibus. Mauris id sem ante, vitae euismod diam. Integer sit amet ligula arcu, ac sollicitudin mauris.</p>
    <p class="flush">Ut ornare, elit vitae congue tristique, felis ligula pretium odio, eget sollicitudin mauris nulla ac leo.</p>
    <p class="flush">viverra vitae tristique nibh faucibus. Mauris id sem ante, vitae euismod diam. Integer sit amet ligula arcu, ac sollicitudin mauris.</p>
    <h3>Our Services</h3>
    <ul class="services">
      <li>Lorem ipsum dolor sit amet, consectetur adipiscing elit.</li>
      <li>Duis at tortor interdum arcu adipiscing mattis.</li>
      <li>Donec sollicitudin libero eu sapien mollis eleifend.</li>
      <li>Mauris nec quam in mi ornare ullamcorper tempus a ipsum.</li>
      <li>Duis placerat nisl vehicula justo pellentesque feugiat.</li>
    </ul>
  </main>
  <div class="column-rule"></div>
  <aside class="newsletter">
    <h2>Join <span>Newsletter</span></h2>
    <div class="newsletter-art" role="img" aria-label="Illustration of a lilac envelope with a purple pen"></div>
    <span class="newsletter-submit">SUBMIT</span>
  </aside>
</div>
<div class="footer-note">Copyright@2011, Lumen Curtain</div>
</body>
</html>
```